Corporate Design für Immobilienfirma
Zielgruppe
Immobilienmakler für Wohn- und Gewerbeimmobilien, Immobilienbewertung, Immobilienberatung, freiberufliche Dozentin
Aufgabenstellung
Das Design sollte hochwertig und seriös wirken, nicht verspielt, stattdessen gradlinig. Bitte jedoch nicht zu exklusiv, da sich der Standort der Firma in einem Gebiet mit weniger Potenzial (keine Ballungsgebiete wie Düsseldort, Hamburg, Köln oder Berlin) befindet. Es muss daher die breite Zielgruppe angesprochen werden, jedoch meine Immobilienkompetenz ausstrahlen. Bitte keine verspielten Häuser oder Dächer im Logo
Das MB sollte möglichst ineinander verschlungen sein, sprich das J und das K sich den "Strich" in der Mitte teilen. Dieser Strich sollte sich dann möglichst nach unten verlängern, sodass hieraus gleichzeitig das "Immobilien" hervorgeht.
Ich bin jung, dynamisch und möchte anders als die Makler hier in der Umgebung arbeiten, bin zudem gelernte Immobilienkauffrau mit angeschlossenen Studium. Diesen Ehrgeiz sollte das Logo möglichst zum Ausdruck bringen.
Mein vollständiger Name lautet Mariella Brunst.
Bei den Farben bin ich nicht festgelegt. Entweder rein dunkleres blau mit grau oder schwarz. Bitte kein orange, grün oder zu bunt.
Was ich zudem gut fände, wenn einzelne Designer versuchen die Silhouette des Velin Museums aus Herford einzubinden, ist jedoch nicht zwingend erforderlich, jedoch würde ich gerne mal so einen Vorschlag prüfen :)
Bei Fragen oder Anregungen stehe ich gerne zur Verfügung.

```html
<!DOCTYPE html>
<html lang="de">
<head>
<meta charset="utf-8">
<title>MB Immobilien – Geschäftsausstattung</title>
<link href="https://fonts.googleapis.com/css2?family=Montserrat:wght@400;500;600&family=Quicksand:wght@400;500;600&display=swap" rel="stylesheet">
<style>
:root{
  --navy:#2c3c66;
  --grey:#777777;
  --grey-light:#8c8c8c;
  --paper:#ffffff;
  --stage:#dedede;
  --text:#555555;
  --window:#ececec;
  --window-line:#d3d3d3;
}
*{box-sizing:border-box;margin:0;padding:0}
html,body{width:1200px;height:3675px;overflow:hidden}
body{background:var(--stage);position:relative;font-family:"Quicksand",sans-serif;color:var(--text)}
.piece{position:absolute;background:var(--paper);box-shadow:0 2px 8px rgba(0,0,0,.15);overflow:hidden}
.brand{font-family:"Montserrat",sans-serif;font-weight:400;letter-spacing:.12em;color:var(--navy);white-space:nowrap;position:absolute}
.center{left:0;right:0;text-align:center}

/* presentation boards */
.board-light{left:78px;top:117px;width:1042px;height:450px}
.board-dark{left:78px;top:567px;width:1042px;height:450px;background:var(--navy)}
.board-light .brand,.board-dark .brand{font-size:58px;top:190px}
.board-dark .brand{color:#fff}

/* business cards */
.card-front{left:74px;top:1057px;width:511px;height:293px}
.card-back{left:614px;top:1057px;width:510px;height:293px;background:var(--grey)}
.card-front .brand{font-size:24px;left:32px;top:60px}
.card-back .brand{color:#fff;font-size:34px;top:124px}
.contact{position:absolute;list-style:none;font-size:11.5px;line-height:17.5px;color:#666}
.contact li{display:flex;align-items:center;gap:8px}
.contact svg{width:11px;height:11px;flex:none;fill:var(--navy)}
.contact .gap{padding-left:19px}
.card-front .contact{left:34px;top:155px}
.person{position:absolute;right:32px;top:212px;text-align:right}
.person .name{font-family:"Montserrat",sans-serif;font-weight:500;font-size:21px;color:var(--navy)}
.person .role{font-size:10.5px;line-height:13px;color:#666}
.card-rule{position:absolute;left:34px;top:261px;width:318px;border-top:1px solid #777}

/* letterhead */
.letter{left:180px;top:1403px;width:840px;height:1158px}
.strip{position:absolute;top:0;right:0;width:20px;height:100%;background:var(--navy)}
.letter .brand{font-size:34px;top:140px;right:20px}
.letter .contact{left:586px;top:250px;font-size:13.5px;line-height:21px;color:#555}
.letter .contact .head{font-weight:600;color:#555;padding-left:21px}
.letter .contact svg{width:13px;height:13px}
.recipient{position:absolute;left:91px;top:380px;font-size:14px;color:#555}
.recipient small{font-size:12px}
.fold{position:absolute;left:0;width:20px;border-top:2px solid var(--navy)}
.body-copy{position:absolute;left:107px;top:483px;width:630px;font-size:14.6px;line-height:21.8px;color:#555}
.body-copy p{margin-bottom:21.8px}
.signature{position:absolute;left:520px;top:825px;width:200px;height:100px;background:linear-gradient(135deg,#f2f2f2,#e4e4e4);border-radius:4px}
.sign-role{position:absolute;left:560px;top:920px;font-weight:600;font-size:14.5px;color:#555}
.letter-footer{position:absolute;left:0;right:20px;top:1080px;text-align:center;font-size:11.5px;line-height:20px;color:#555}

/* envelope front */
.envelope-front{left:113px;top:2619px;width:974px;height:440px}
.envelope-front .brand{font-size:33px;right:52px;top:140px}
.address-window{position:absolute;left:69px;top:243px;width:318px;height:126px;background:var(--window);border:3px solid var(--window-line);border-radius:8px;padding:20px 24px;font-family:Arial,sans-serif;font-size:12px;line-height:14px;color:#444}
.address-window .date{margin-bottom:16px}

/* envelope back */
.envelope-back{left:113px;top:3118px;width:974px;height:439px}
.flap{position:absolute;left:0;top:0;width:100%;height:146px;background:var(--navy);border-radius:0 0 75px 75px}
.flap .brand{color:#fff;font-size:30px;top:52px}
.back-name{font-size:26px;left:54px;top:372px}
.back-rule{position:absolute;left:313px;top:399px;width:424px;border-top:1px solid #777}
.back-url{position:absolute;left:744px;top:390px;font-size:13.5px;color:#666}
</style>
</head>
<body>

<svg width="0" height="0" style="position:absolute">
  <defs>
    <symbol id="i-pin" viewBox="0 0 12 12"><path d="M6 0a4 4 0 0 0-4 4c0 3 4 8 4 8s4-5 4-8a4 4 0 0 0-4-4zm0 5.6A1.6 1.6 0 1 1 6 2.4a1.6 1.6 0 0 1 0 3.2z"/></symbol>
    <symbol id="i-phone" viewBox="0 0 12 12"><path d="M0 4c0-2 3-3 6-3s6 1 6 3v1H9V4H3v1H0zM2 6h8l1 5H1z"/></symbol>
    <symbol id="i-fax" viewBox="0 0 12 12"><path d="M3 0h6v4H3zM0 5h12v6H0zm2 2v2h8V7z"/></symbol>
    <symbol id="i-mail" viewBox="0 0 12 12"><path d="M0 2h12v8H0zm1 1v.5l5 3.5 5-3.5V3z"/></symbol>
    <symbol id="i-web" viewBox="0 0 12 12"><circle cx="6" cy="6" r="6"/></symbol>
  </defs>
</svg>

<section class="piece board-light">
  <div class="brand center">MB IMMOBILIEN</div>
</section>
<section class="piece board-dark">
  <div class="brand center">MB IMMOBILIEN</div>
</section>

<section class="piece card-front">
  <div class="brand">MB IMMOBILIEN</div>
  <ul class="contact">
    <li><svg><use href="#i-pin"/></svg>Lindenallee 48</li>
    <li class="gap">32052 Herford</li>
    <li><svg><use href="#i-phone"/></svg>05221 4410-200</li>
    <li><svg><use href="#i-fax"/></svg>05221 4410-200</li>
    <li><svg><use href="#i-mail"/></svg>info@mb-immobilien.de</li>
    <li><svg><use href="#i-web"/></svg>www.mb-immobilien.de</li>
  </ul>
  <div class="person">
    <div class="name">Lukas Ferber</div>
    <div class="role">Dipl.-Bertrw. (DW)<br>Geschaftsfuhrer</div>
  </div>
  <div class="card-rule"></div>
</section>
<section class="piece card-back">
  <div class="brand center">MB IMMOBILIEN</div>
</section>

<section class="piece letter">
  <div class="strip"></div>
  <div class="brand center">MB IMMOBILIEN</div>
  <ul class="contact">
    <li class="head">MB IMMOBILIEN</li>
    <li><svg><use href="#i-pin"/></svg>Lindenallee 48</li>
    <li class="gap">32052 Herford</li>
    <li><svg><use href="#i-phone"/></svg>05221 4410-200</li>
    <li><svg><use href="#i-fax"/></svg>05221 4410-200</li>
    <li><svg><use href="#i-mail"/></svg>info@yourwebsite.com</li>
    <li><svg><use href="#i-web"/></svg>www.yourwebsite.com</li>
  </ul>
  <div class="recipient">Rad und Freizeit Haus -<small>Lindenallee 48-32052 Herford</small></div>
  <div class="fold" style="top:461px"></div>
  <div class="fold" style="top:825px"></div>
  <div class="body-copy">
    <p>Lorem ipsum dolor sit amet, consectetur adipiscing elit. Fusce dignissim pretium consectetur. Curabitur tempor posuere massa in varius. Pellentesque viverra nibh eu vehicula mattis. Nullam porta facilisis justo, a feugiat dolor sodales sed. Vestibulum neque nisi, elementum tincidunt metus sit amet, egestas bibendum enim. Aenean a blandit elit, vel rutrum mi. Nunc dapibus turpis sed massa aliquet tincidunt.</p>
    <p>Pellentesque id neque ligula. Nullam posuere, ligula a mattis posuere, lacus nisl adipiscing nunc, eu congue justo est ut diam. Nam quam nibh, dignissim non consequat in, semper eget purus. Nulla arcu sapien, viverra vitae metus tempor, congue ornare diam.</p>
    <p>Pellentesque vel nibh tempus, ullamcorper tortor sed, bibendum augue. Phasellus sollicitudin justo et quam aliquam sollicitudin. Sed eget nibh mollis, mattis sem et, viverra nulla.</p>
  </div>
  <div class="signature" role="img" aria-label="Handschriftliche Unterschrift"></div>
  <div class="sign-role">Creative Art Director</div>
  <div class="letter-footer">
    MB IMMOBILIEN &nbsp;I&nbsp; Lindenallee 48 &nbsp;I&nbsp; 32052 Herford<br>
    Telefon: 05221 4410-200 &nbsp;I&nbsp; Telefax: 05221 4410-200 &nbsp;I&nbsp; email: mb-immobilien.de &nbsp;I&nbsp; www.mb-immobilien.de<br>
    Bank international: Stadtsparkasse Nordtal &nbsp;I&nbsp; BIC: NORDDE21XXX &nbsp;I&nbsp; IBAN: DE00 1200 3400 5600 7800 91
  </div>
</section>

<section class="piece envelope-front">
  <div class="strip"></div>
  <div class="brand">MB IMMOBILIEN</div>
  <div class="address-window">
    <div class="date">[Click Here to Select a Date]</div>
    [Recipient Name]<br>[Recipient Street Address, City, ST ZIP Code]<br>[Recipient Email]
  </div>
</section>

<section class="piece envelope-back">
  <div class="flap"><div class="brand center">MB</div></div>
  <div class="brand back-name">MB IMMOBILIEN</div>
  <div class="back-rule"></div>
  <div class="back-url">www.mb-immobilien.de</div>
</section>

</body>
</html>
```